Business Cards

Need a neat design for a new business card

Industry/Entity Type

Residential Construction

Contact Information for Business Card

Company Name- KORV Construction Inc.
Owner- Daniel Pruitt
Phone number- (555)270-4418
Email- korvcobuilds@mailbox-example.com
Facebook- www.socialpage-example.com/korvcobuilds

Colors
fefdec

```html
<!DOCTYPE html>
<html lang="en">
<head>
<meta charset="utf-8">
<title>KORV Construction Inc. — Business Card</title>
<link rel="stylesheet" href="https://fonts.googleapis.com/css2?family=Roboto:wght@400;500;700&display=swap">
<style>
  :root {
    --page-bg: #ecebe8;
    --card-white: #ffffff;
    --card-black: #050505;
    --ink: #1a1a1a;
    --ink-muted: #8a8a8a;
    --ink-light: #ffffff;
    --pattern-top: #2a2a2a;
    --pattern-bottom: #0a0a0a;
    --card-shadow: rgba(0, 0, 0, 0.18);
  }
  * { box-sizing: border-box; margin: 0; padding: 0; }
  html, body {
    width: 1200px;
    height: 900px;
    overflow: hidden;
    background: var(--page-bg);
    font-family: "Roboto", Arial, sans-serif;
  }
  .card-set {
    position: relative;
    width: 1200px;
    height: 900px;
  }
  .card {
    position: absolute;
    top: 100px;
    width: 400px;
    height: 700px;
    box-shadow: 0 10px 30px var(--card-shadow);
    overflow: hidden;
  }
  .card--front { left: 170px; background: var(--card-white); }
  .card--back { left: 630px; background: var(--card-black); }

  .brand-name {
    position: absolute;
    left: 0;
    right: 0;
    text-align: center;
    font-weight: 500;
    letter-spacing: 0.06em;
  }
  .card--front .brand-name {
    top: 108px;
    font-size: 26px;
    color: var(--ink);
  }
  .card--back .brand-name {
    bottom: 92px;
    font-size: 24px;
    color: var(--ink-light);
  }

  .owner {
    position: absolute;
    top: 428px;
    left: 0;
    right: 0;
    text-align: center;
  }
  .owner__name {
    font-size: 18px;
    font-weight: 700;
    letter-spacing: 0.02em;
    color: var(--ink);
    text-transform: uppercase;
  }
  .owner__role {
    margin-top: 2px;
    font-size: 13px;
    color: var(--ink-muted);
  }
  .contact {
    position: absolute;
    top: 512px;
    left: 0;
    right: 0;
    list-style: none;
    text-align: center;
    font-size: 14px;
    color: var(--ink);
  }
  .contact li { margin-bottom: 14px; }

  .back-pattern {
    position: absolute;
    top: 0;
    left: 0;
    width: 400px;
    height: 470px;
    background: linear-gradient(180deg, var(--pattern-top) 0%, var(--pattern-bottom) 100%);
  }
</style>
</head>
<body>
  <main class="card-set">
    <section class="card card--front" aria-label="Card front">
      <div class="brand-name">KORV Construction Inc.</div>
      <div class="owner">
        <p class="owner__name">Daniel Pruitt</p>
        <p class="owner__role">Owner</p>
      </div>
      <ul class="contact">
        <li>(555)270-4418</li>
        <li>korvcobuilds@mailbox-example.com</li>
        <li>www.socialpage-example.com/korvcobuilds</li>
      </ul>
    </section>

    <section class="card card--back" aria-label="Card back">
      <div class="back-pattern" role="img" aria-label="Repeating diagonal company name pattern fading from grey to black"></div>
      <div class="brand-name">KORV Construction Inc.</div>
    </section>
  </main>
</body>
</html>
```